" A empresa foi criada para comercializar e prestar serviços especializados em softwares voltados para infraestrutura de tecnologia. Nosso ramo de atuação será a venda e entrega de soluções para clientes que possuem infraestrutura de tecnologia própria (on-premisses) e clientes que não possuem infraestrutura, utilizando nuvens públicas como TNQ e Morvek. "

```html
<!DOCTYPE html>
<html lang="pt-BR">
<head>
<meta charset="UTF-8">
<title>Veltrix – Cartão de Visita</title>
<link rel="stylesheet" href="https://fonts.googleapis.com/css2?family=Montserrat:wght@400;500;600;700&display=swap">
<style>
  :root {
    --navy: #2a2f4f;
    --navy-deep: #23284a;
    --cyan: #1c9fd0;
    --cyan-light: #3bb8e2;
    --white: #ffffff;
    --ink: #3a3f55;
    --grey: #8a8fa0;
    --page: #e9eaec;
  }
  * { margin: 0; padding: 0; box-sizing: border-box; }
  html, body { width: 1200px; height: 1200px; overflow: hidden; }
  body {
    background: var(--page);
    font-family: "Montserrat", sans-serif;
    position: relative;
  }
  .card {
    position: absolute;
    left: 150px;
    width: 900px;
    height: 500px;
    border-radius: 34px;
    overflow: hidden;
    box-shadow: 0 6px 18px rgba(0,0,0,0.12);
  }
  .card--front { top: 70px; background: var(--navy); }
  .card--back { top: 630px; background: var(--white); }

  .brand { display: flex; align-items: center; gap: 18px; }
  .brand__square { width: 46px; height: 46px; background: var(--cyan); }
  .brand__text { display: flex; flex-direction: column; }
  .brand__name {
    font-weight: 700;
    font-size: 56px;
    letter-spacing: 3px;
    line-height: 1;
  }
  .brand__tagline {
    font-weight: 500;
    font-size: 14px;
    letter-spacing: 3.2px;
    margin-top: 6px;
  }

  .card--front .brand {
    position: absolute;
    left: 210px;
    top: 150px;
  }
  .card--front .brand__name { color: var(--white); }
  .card--front .brand__tagline { color: var(--cyan-light); }
  .front__stripe { position: absolute; left: 0; bottom: 0; width: 900px; height: 500px; }
  .front__corner-mark {
    position: absolute;
    right: 48px;
    top: 290px;
    width: 34px;
    height: 34px;
    background: var(--cyan-light);
  }

  .card--back .brand { position: absolute; left: 50px; top: 60px; }
  .card--back .brand__name { color: var(--navy); font-size: 50px; }
  .card--back .brand__tagline { color: var(--navy); font-size: 12.5px; }
  .card--back .brand__square { width: 40px; height: 40px; }

  .back__edge {
    position: absolute;
    right: 0;
    top: 0;
    width: 34px;
    height: 100%;
    background: var(--navy);
  }
  .back__edge::before {
    content: "";
    position: absolute;
    left: -8px;
    top: 0;
    width: 8px;
    height: 100%;
    background: var(--cyan);
  }

  .person {
    position: absolute;
    right: 100px;
    top: 190px;
    text-align: right;
  }
  .person__name {
    color: var(--cyan);
    font-weight: 600;
    font-size: 24px;
    letter-spacing: 1px;
  }
  .person__role {
    color: var(--grey);
    font-size: 13px;
    letter-spacing: 1.5px;
    margin-top: 4px;
  }

  .contacts {
    position: absolute;
    right: 76px;
    top: 270px;
    list-style: none;
  }
  .contacts__item {
    display: flex;
    align-items: center;
    justify-content: flex-end;
    gap: 14px;
    height: 44px;
    color: var(--ink);
    font-size: 20px;
  }
  .contacts__icon { width: 22px; height: 22px; flex: none; }
</style>
</head>
<body>

<section class="card card--front" aria-label="Frente do cartão">
  <svg class="front__stripe" viewBox="0 0 900 500" aria-hidden="true">
    <polygon points="0,422 900,352 900,366 0,436" fill="var(--cyan)"/>
    <polygon points="0,436 900,366 900,500 0,500" fill="var(--navy-deep)"/>
  </svg>
  <div class="brand">
    <span class="brand__square"></span>
    <div class="brand__text">
      <span class="brand__name">VELTRIX</span>
      <span class="brand__tagline">SOLUÇÕES EM TECNOLOGIA</span>
    </div>
  </div>
  <span class="front__corner-mark"></span>
</section>

<section class="card card--back" aria-label="Verso do cartão">
  <div class="brand">
    <span class="brand__square"></span>
    <div class="brand__text">
      <span class="brand__name">VELTRIX</span>
      <span class="brand__tagline">SOLUÇÕES EM TECNOLOGIA</span>
    </div>
  </div>

  <div class="person">
    <p class="person__name">NOME SOBRENOME</p>
    <p class="person__role">CARGO/FUNÇÃO</p>
  </div>

  <ul class="contacts">
    <li class="contacts__item">
      <span>nome@empresa.com.br</span>
      <svg class="contacts__icon" viewBox="0 0 22 22" aria-hidden="true">
        <circle cx="11" cy="11" r="11" fill="var(--cyan)"/>
        <rect x="5.5" y="7" width="11" height="8" rx="1" fill="none" stroke="#fff" stroke-width="1.4"/>
        <polyline points="5.5,7.5 11,11.5 16.5,7.5" fill="none" stroke="#fff" stroke-width="1.4"/>
      </svg>
    </li>
    <li class="contacts__item">
      <span>99 9999-0000</span>
      <svg class="contacts__icon" viewBox="0 0 22 22" aria-hidden="true">
        <circle cx="11" cy="11" r="11" fill="var(--cyan)"/>
        <path d="M7.5 6 L9.5 6 L10.3 8.6 L9 9.6 Q10 12 12.4 13 L13.4 11.7 L16 12.5 L16 14.5 Q15.5 16 13.8 16 Q6 15 6 8.2 Q6 6.5 7.5 6 Z" fill="#fff"/>
      </svg>
    </li>
    <li class="contacts__item">
      <span>99 99999-9999</span>
      <svg class="contacts__icon" viewBox="0 0 22 22" aria-hidden="true">
        <circle cx="11" cy="11" r="11" fill="var(--cyan)"/>
        <rect x="8" y="5" width="6" height="12" rx="1.2" fill="none" stroke="#fff" stroke-width="1.4"/>
        <circle cx="11" cy="14.8" r="0.8" fill="#fff"/>
      </svg>
    </li>
    <li class="contacts__item">
      <span>Rua do Projeto, 999</span>
      <svg class="contacts__icon" viewBox="0 0 22 22" aria-hidden="true">
        <circle cx="11" cy="11" r="11" fill="var(--cyan)"/>
        <path d="M11 17 Q6.5 12 6.5 9.5 A4.5 4.5 0 0 1 15.5 9.5 Q15.5 12 11 17 Z" fill="#fff"/>
        <circle cx="11" cy="9.5" r="1.7" fill="var(--cyan)"/>
      </svg>
    </li>
  </ul>

  <div class="back__edge"></div>
</section>

</body>
</html>
```